Legal Stationary

A full set of stationery is required
The image and logo, along with colour, are set and attached.
The style should be modern, clean, and corporate. Not just a basic template off the web.
In addition to the address/website/email/phone fields for DX and KWT number, with the text “the firm is authorised and regulated by the KWT”
All files in all formats will be needed to allow editing after. Initial setup of templates will be required, and details for 4 business cards will be supplied.
Target Market(s)
Consumers of legal services
Industry/Entity Type
Legal

```html
<!DOCTYPE html>
<html lang="en">
<head>
<meta charset="utf-8">
<title>Holt Law Stationery</title>
<link href="https://fonts.googleapis.com/css2?family=Montserrat:wght@400;500;700&family=Roboto:wght@300;400;500&display=swap" rel="stylesheet">
<style>
:root{
  --brand:#233c96;
  --ink:#444;
  --muted:#6b6b6b;
  --paper:#fff;
  --bg:#dcdde0;
  --row:#f2f3f4;
}
*{box-sizing:border-box;margin:0;padding:0}
html,body{width:1200px;height:943px;overflow:hidden;background:var(--bg)}
body{font-family:'Roboto',sans-serif;color:var(--ink)}
.stage{position:relative;width:1200px;height:943px}
.sheet{position:absolute;background:var(--paper);box-shadow:3px 4px 8px rgba(0,0,0,.18)}
.wordmark{font-family:'Roboto',sans-serif;font-weight:500;color:var(--brand);letter-spacing:.02em;text-align:center;white-space:nowrap}
.wordmark.light{color:#fff}

/* business card */
.card{width:326px;height:186px;border-radius:10px}
.card-front{left:66px;top:93px}
.card-front .wordmark{position:absolute;left:0;right:0;top:22px;font-size:40px;line-height:46px}
.card-name{position:absolute;right:180px;top:110px;text-align:right}
.card-name h1{font-family:'Montserrat',sans-serif;font-weight:700;font-size:15.5px;color:var(--brand);line-height:18px}
.card-name p{font-size:12px;line-height:14px;color:#333}
.card-divider{position:absolute;left:158px;top:87px;width:1px;height:81px;background:#555}
.card-details{position:absolute;left:169px;top:86px;font-size:9px;line-height:10.6px;color:#444;font-weight:400}
.card-details ul{list-style:none;margin-top:4px}
.card-details li{display:flex;align-items:center;gap:4px;line-height:11.5px}
.card-details svg{width:8px;height:8px;fill:var(--brand)}
.card-back{left:66px;top:290px;background:var(--brand)}
.card-back .wordmark{position:absolute;left:0;right:0;top:68px;font-size:40px;line-height:48px}
.legal-note{font-size:5.3px;line-height:8.4px;color:#fff;text-align:center;font-weight:300}
.card-back .legal-note{position:absolute;left:28px;right:28px;top:142px}

/* letterhead */
.letterhead{left:413px;top:90px;width:273px;height:385px}
.letterhead .wordmark{position:absolute;left:0;right:0;top:20px;font-size:20px;line-height:24px}
.letter-body{position:absolute;left:28px;top:93px;width:217px;font-family:'Montserrat',sans-serif;font-size:4.2px;line-height:6.3px;color:#666}
.letter-body p{margin-bottom:6.3px;text-align:justify}
.signature{margin-top:6px;width:28px;height:26px;background:linear-gradient(135deg,#eee,#d9d9d9)}
.doc-rule{position:absolute;left:28px;right:28px;top:341px;height:1px;background:#999}
.doc-footer{position:absolute;left:0;right:0;text-align:center;font-size:5.2px;line-height:7.4px;color:#444}
.doc-footer .contacts{display:flex;justify-content:center;gap:4px;align-items:center}
.doc-footer svg{width:5px;height:5px;fill:var(--brand)}
.letterhead .doc-footer{top:350px}

/* envelopes */
.envelope{width:428px}
.envelope-back{left:705px;top:94px;height:200px}
.envelope-back .wordmark{position:absolute;left:34px;width:101px;top:28px;font-size:20px;line-height:24px}
.envelope-back address{position:absolute;left:24px;width:121px;top:58px;font-style:normal;font-weight:400;text-align:center;font-size:8px;line-height:10px;color:#444}
.envelope-front{left:705px;top:311px;height:204px}
.envelope-front svg.flap{position:absolute;left:0;top:0;width:428px;height:76px}
.envelope-front .wordmark{position:absolute;left:0;right:0;top:20px;font-size:22px;line-height:26px}
.envelope-front .legal-note{position:absolute;left:65px;width:298px;top:154px;color:#666;text-align:justify;text-align-last:center}

/* invoice */
.invoice{left:68px;top:489px;width:298px;height:416px}
.invoice .wordmark{position:absolute;left:0;right:0;top:24px;font-size:21px;line-height:25px}
.invoice-title{position:absolute;left:20px;top:66px;font-family:'Montserrat',sans-serif;font-weight:500;font-size:8.5px;color:var(--brand)}
.invoice-date{position:absolute;left:218px;top:69px;font-family:'Montserrat',sans-serif;font-weight:500;font-size:5px;color:#222}
.field{position:absolute;left:20px;right:20px;display:flex;align-items:flex-end;gap:3px;font-family:'Montserrat',sans-serif;font-size:5.3px;color:#555}
.field span.line{flex:1;border-bottom:.6px solid #777;height:5px}
.items{position:absolute;left:20px;top:121px;width:258px;height:183px;border:.8px solid var(--brand);background:repeating-linear-gradient(#f6f6f7 0 15px,#eeeff0 15px 30px)}
.items-head{display:grid;grid-template-columns:34px 135px 44px 1fr;height:17px;background:var(--brand);color:#fff;font-family:'Montserrat',sans-serif;font-weight:500;font-size:6px;align-items:center;text-align:center}
.items .col{position:absolute;top:17px;bottom:0;width:.8px;background:var(--brand)}
.totals{position:absolute;left:189px;top:305px;width:89px;border:.8px solid var(--brand);border-top:none}
.totals div{display:grid;grid-template-columns:44px 1fr;height:15px;border-top:.8px solid var(--brand);font-family:'Montserrat',sans-serif;font-size:5px;color:#333}
.totals span{display:flex;align-items:center;padding-left:7px}
.totals span+span{border-left:.8px solid var(--brand)}
.payment{position:absolute;left:20px;top:315px;width:162px;display:flex;justify-content:space-between;font-family:'Montserrat',sans-serif;font-size:5px;color:#555;white-space:nowrap}
.payment label{display:flex;align-items:center;gap:2px}
.payment i{width:6px;height:6px;border:.7px solid var(--brand)}
.sign-note{position:absolute;left:20px;top:335px;font-family:'Montserrat',sans-serif;font-size:5.3px;line-height:7.6px;color:#555}
.invoice .doc-footer{top:380px}
</style>
</head>
<body>
<div class="stage">

  <svg width="0" height="0" style="position:absolute">
    <defs>
      <symbol id="i-phone" viewBox="0 0 10 10"><path d="M1 4c0-2 2-3 4-3s4 1 4 3H7V3H3v1zM2 5h6l1 4H1z"/></symbol>
      <symbol id="i-mobile" viewBox="0 0 10 10"><path d="M2.5 0h5v10h-5zM3.5 1v7h3V1z"/></symbol>
      <symbol id="i-mail" viewBox="0 0 10 10"><path d="M0 2h10v1L5 6 0 3zM0 4l5 3 5-3v4H0z"/></symbol>
      <symbol id="i-web" viewBox="0 0 10 10"><circle cx="5" cy="5" r="5"/></symbol>
    </defs>
  </svg>

  <!-- business card front -->
  <section class="sheet card card-front">
    <div class="wordmark">HOLT LAW</div>
    <div class="card-name">
      <h1>SAM PORTER</h1>
      <p>Director</p>
    </div>
    <div class="card-divider"></div>
    <div class="card-details">
      <p>HOLT LAW First Floor<br>Ashby House Mill<br>Street Harwood HD9 4XY</p>
      <ul>
        <li><svg><use href="#i-phone"/></svg>0330 0000 111</li>
        <li><svg><use href="#i-mobile"/></svg>07700 900123</li>
        <li><svg><use href="#i-mail"/></svg>info@holtlaw.example</li>
        <li><svg><use href="#i-web"/></svg>www.holtlaw.example</li>
      </ul>
    </div>
  </section>

  <!-- business card back -->
  <section class="sheet card card-back">
    <div class="wordmark light">HOLT LAW</div>
    <p class="legal-note">Holt Law is a trading style of Larkspur Law Limited, registered in England with company number 10000001, authorised and regulated by the KWT (No 800000). Our registered office is 4-6 Abbey Terrace, Farnley, FA2 7QT - VAT number 300000000</p>
  </section>

  <!-- letterhead -->
  <section class="sheet letterhead">
    <div class="wordmark">HOLT LAW</div>
    <div class="letter-body">
      <p>Dear customer,</p>
      <p>Lorem ipsum dolor sit amet, consectetur adipisicing elit, sed do eiusmod tempor incididunt ut labore et dolore magna aliqua. Ut enim ad minim veniam, quis nostrud exercitation ullamco laboris nisi ut aliquip ex ea commodo consequat. Duis aute irure dolor in reprehenderit in voluptate velit esse cillum dolore eu fugiat nulla pariatur. Excepteur sint occaecat cupidatat non proident, sunt in culpa qui officia deserunt mollit anim id est laborum.</p>
      <p>Lorem ipsum dolor sit amet, consectetur adipisicing elit, sed do eiusmod tempor incididunt ut labore et dolore magna aliqua. Ut enim ad minim veniam, quis nostrud exercitation ullamco laboris nisi ut aliquip ex ea commodo consequat. Duis aute irure dolor in reprehenderit in voluptate velit esse cillum dolore eu fugiat nulla pariatur. Excepteur sint occaecat cupidatat non proident, sunt in culpa qui officia deserunt mollit anim id est laborum.</p>
      <p>Lorem ipsum dolor sit amet, consectetur adipisicing elit, sed do eiusmod tempor incididunt ut labore et dolore magna aliqua. Ut enim ad minim veniam, quis nostrud exercitation ullamco laboris nisi ut aliquip ex ea commodo consequat. Duis aute irure dolor in reprehenderit in voluptate velit esse cillum dolore eu fugiat nulla pariatur. Excepteur sint occaecat cupidatat non proident, sunt in culpa qui officia deserunt mollit anim id est laborum.</p>
      <p>Lorem ipsum dolor sit amet, consectetur adipisicing elit, sed do eiusmod tempor incididunt ut labore et dolore magna aliqua. Ut enim ad minim veniam, quis nostrud exercitation ullamco laboris nisi ut aliquip ex ea commodo consequat. Duis aute irure dolor in reprehenderit.</p>
      <p>Yours Sincerely,</p>
      <p style="margin-top:10px;margin-bottom:0">Mark Lee<br>General Director</p>
      <div class="signature" role="img" aria-label="Handwritten signature of the director"></div>
    </div>
    <div class="doc-rule"></div>
    <div class="doc-footer">
      <p>HOLT LAW First Floor Ashby House Mill Street Harwood HD9 4XY</p>
      <p class="contacts"><svg><use href="#i-phone"/></svg>0330 0000 111 <svg><use href="#i-mobile"/></svg>07700 900123 <svg><use href="#i-mail"/></svg>info@holtlaw.example</p>
      <p>www.holtlaw.example</p>
    </div>
  </section>

  <!-- envelope, address side -->
  <section class="sheet envelope envelope-back">
    <div class="wordmark">HOLT LAW</div>
    <address>HOLT LAW First Floor<br>Ashby House Mill<br>Street Harwood HD9 4XY</address>
  </section>

  <!-- envelope, flap side -->
  <section class="sheet envelope envelope-front">
    <svg class="flap" viewBox="0 0 428 76" aria-hidden="true">
      <path fill="#233c96" d="M0 0H428L405 38Q398 48 386 50L222 74Q214 76 206 74L42 50Q30 48 23 38Z"/>
    </svg>
    <div class="wordmark light">HOLT LAW</div>
    <p class="legal-note">Holt Law is a trading style of Larkspur Law Limited, registered in England with company number 10000001, authorised and regulated by the KWT (No 800000). Our registered office is 4-6 Abbey Terrace, Farnley, FA2 7QT - VAT number 300000000</p>
  </section>

  <!-- invoice -->
  <section class="sheet invoice">
    <div class="wordmark">HOLT LAW</div>
    <div class="invoice-title">INVOICE # :</div>
    <div class="invoice-date">DATE :</div>
    <div class="field" style="top:78px">Customer : <span class="line"></span></div>
    <div class="field" style="top:90px">Address : <span class="line"></span></div>
    <div class="field" style="top:102px">Phone : <span class="line"></span> Fax : <span class="line" style="flex:.9"></span></div>

    <div class="items">
      <div class="items-head"><span>QTY</span><span>DESCRIPTION</span><span>PRICE</span><span>AMOUNT</span></div>
      <div class="col" style="left:34px"></div>
      <div class="col" style="left:169px"></div>
      <div class="col" style="left:213px"></div>
    </div>

    <div class="totals">
      <div><span>SUB TOTAL</span><span></span></div>
      <div><span>GST #</span><span></span></div>
      <div><span>SUBTOTAL</span><span></span></div>
    </div>

    <div class="payment">
      <label><i></i>CREDIT</label>
      <label><i></i>CARD</label>
      <label><i></i>DEBIT</label>
      <label><i></i>CASH</label>
      <label><i></i>CHEQUE</label>
    </div>
    <p class="sign-note">Signature Indicates<br>Acceptance of Price and term</p>

    <div class="doc-footer">
      <p>HOLT LAW First Floor Ashby House Mill Street Harwood HD9 4XY</p>
      <p class="contacts"><svg><use href="#i-phone"/></svg>0330 0000 111 <svg><use href="#i-mobile"/></svg>07700 900123 <svg><use href="#i-mail"/></svg>info@holtlaw.example</p>
      <p>www.holtlaw.example</p>
    </div>
  </section>

</div>
</body>
</html>
```